A disruptive product that needs to communicate modernity and tradition at the same time

The product combines MODERNITY and TRADITION in a magnitude difficult to express. It also has as target users personas that can be very different from each other.

DRIVEN BY INNOVATION, ROOTED IN TRADITION, is probably what the design should be able to transfer.

Buyer and user of such line of product shall be attracetd because they think at the same time they are buying something revolutionary and disruptive but at the same time reassured that they are to eat 1005 natural and that al that resides in the 100% of the company that has developed Nebulfino.

The contest has the objetive to design a complete new product line that will replace an existing one.

We voluntarely did not express any specific style or color as we want designers to work on a zero-base style minded so as to collect the maximum ideas possible from which to choose the one that we will consider that responds the best.

As already said, the line includes a very wide range of items and we are now looking for a base packaging design that would be common to all of them.

We know our objective is difficult and only the very best designers will be able to accept the challenge: the designer is asked to create a "disrputive new design" for a "disruptive new product" yet connecting it to the 100 years of the comapny that is producing it.

Main logo is the name of the product that today is NEBULFINO (but we accept inspirations also for changes).

The company logo Corvalda is to be just a signature and not the main product logo.

See existing product at www.nebulfino-esempio.it

Target Market(s)

PERSONAS:
The personas (target) are extremely diverse and include many types that we could summarise:

a. Household…. open to innovation and paying attention to what makes easier its cooking but also healthier

b. Health conscious … always paying attention to health benefits that they can have from their food everyday

c. FIT Maniac … always paying attention to calories but also to health benefits that they can have from their food everyday

d. Amatorial masterchef … all sort of people (singles of any age, women or men managers, just people of al sort of culture and social census have discovered through popular media TV reality that cooking can be: self fulfilling, fascinating, seductive, socializing etc etc.

e. Professional chefs ….. new to the spray concept as well as those that already uses them just as NON-STICK product that are willing to use Spray as an enhancer of their dishes, using flavored oils for example, or using real 100% extra virgin olive oil that multiplies its aroma through the spraying process as related to normal pouring from a bottle.

f. Silver Age …. , people live much longer today and retired persons are not anymore sitting awaiting for their end to come: they are active, they travel, they are open to seep as much as they can from modern times and are extremely conscious about healthiness of what they cook but also they look for simplicity in cooking activity.

Industry/Entity Type

Food Store

Logo Text

NEBULFINO plus a second naming suggested by designer

Colors

Designer to choose colors to be used in the design.

```html
<!DOCTYPE html>
<html lang="en">
<head>
<meta charset="utf-8">
<title>Nebulfino – Avocado Oil Spray Label</title>
<link href="https://fonts.googleapis.com/css2?family=Marcellus&family=Roboto+Condensed:wght@700&family=Share+Tech&display=swap" rel="stylesheet">
<style>
  :root {
    --bg: #e4e4e4;
    --green: #1f6b35;
    --green-dark: #134d24;
    --green-light: #2f8a47;
    --white: #f7f7f7;
    --silver: #cfd2d4;
    --silver-dark: #9ea3a6;
    --gold: #d9a62e;
    --gold-dark: #8a6212;
    --ink: #1c1c1c;
  }
  * { margin: 0; padding: 0; box-sizing: border-box; }
  html, body { width: 1035px; height: 1200px; overflow: hidden; }
  body {
    background: var(--bg);
    font-family: "Marcellus", serif;
    position: relative;
  }
  .label {
    position: absolute;
    left: 287px; top: 80px;
    width: 460px; height: 1040px;
    background: linear-gradient(90deg, #e2e2e2 0%, var(--white) 35%, #ffffff 55%, #e6e6e6 100%);
    overflow: hidden;
    border-radius: 6px;
  }
  .label-top {
    position: absolute; left: 0; top: 0; width: 460px; height: 330px;
  }
  .spray-band {
    position: absolute; left: 0; top: 62px; width: 100%; height: 54px;
    background: linear-gradient(180deg, #f1f1f1, var(--silver) 60%, #e9e9e9);
    border-top: 2px solid var(--silver-dark);
    border-bottom: 2px solid var(--silver-dark);
    display: flex; align-items: center; justify-content: center;
    color: var(--green-dark); font-size: 24px; letter-spacing: 1px;
  }
  .brand-plate {
    position: absolute; left: 70px; top: 170px; width: 320px; height: 62px;
    background: var(--green-light);
    border: 3px solid var(--white);
    border-radius: 6px;
    display: flex; align-items: center; justify-content: center;
    color: var(--white); font-size: 30px; letter-spacing: 1px;
  }
  .product-name {
    position: absolute; left: 0; top: 370px; width: 100%;
    text-align: center; color: var(--green-dark);
    line-height: 1.05;
  }
  .product-name .pct { display: block; font-size: 46px; }
  .product-name .pure { display: block; font-size: 46px; }
  .product-name .fruit { display: block; font-size: 64px; letter-spacing: 1px; }
  .product-name .oil { display: block; font-size: 46px; }
  .tag {
    position: absolute; left: 128px; top: 655px; width: 204px; height: 48px;
    background: linear-gradient(180deg, #f0c65a, var(--gold) 55%, #b9871c);
    border: 2px dashed var(--gold-dark);
    outline: 3px solid var(--gold);
    display: flex; align-items: center; justify-content: center;
    font-family: "Share Tech", sans-serif; font-size: 30px; color: var(--ink);
    transform: rotate(-2deg);
  }
  .claim-band {
    position: absolute; left: 0; top: 728px; width: 100%; height: 120px;
    background: linear-gradient(180deg, var(--green-light), var(--green) 50%, var(--green-dark));
    text-align: center; color: var(--white);
    padding-top: 14px;
  }
  .claim-band .sub { font-size: 22px; line-height: 1.2; }
  .claim-band .main { font-size: 27px; line-height: 1.15; }
  .claim-tab {
    position: absolute; left: 125px; top: 848px; width: 210px; height: 40px;
    background: linear-gradient(180deg, #eeeeee, var(--silver));
    border: 2px solid var(--silver-dark); border-top: none;
    border-radius: 0 0 14px 14px;
    display: flex; align-items: center; justify-content: center;
    font-size: 22px; color: var(--ink);
  }
  .badge {
    position: absolute; top: 905px; width: 58px; height: 58px;
    border-radius: 50%; border: 2px solid #555; background: #f3f3f3;
  }
  .badge-left { left: 48px; }
  .badge-right { right: 48px; }
  .caution {
    position: absolute; left: 0; top: 962px; width: 100%;
    text-align: center; font-family: "Roboto Condensed", sans-serif;
    font-size: 11px; color: var(--ink);
  }
  .net {
    position: absolute; left: 0; top: 1005px; width: 100%;
    text-align: center; font-family: "Roboto Condensed", sans-serif;
    font-size: 13px; color: var(--ink);
  }
</style>
</head>
<body>
  <main class="label">
    <svg class="label-top" viewBox="0 0 460 330" width="460" height="330" aria-hidden="true">
      <defs>
        <linearGradient id="topGreen" x1="0" y1="0" x2="1" y2="0">
          <stop offset="0" stop-color="#134d24"/>
          <stop offset="0.45" stop-color="#2a7c40"/>
          <stop offset="1" stop-color="#134d24"/>
        </linearGradient>
      </defs>
      <path d="M0 0 H460 V300 C380 270 300 265 230 285 C150 308 70 300 0 290 Z" fill="url(#topGreen)"/>
      <path d="M0 290 C70 300 150 308 230 285 C300 265 380 270 460 300" fill="none" stroke="#cfd2d4" stroke-width="8"/>
    </svg>
    <div class="spray-band">NATURAL SPRAY</div>
    <div class="brand-plate">NEBULFINO</div>

    <h1 class="product-name">
      <span class="pct">100%</span>
      <span class="pure">PURE</span>
      <span class="fruit">AVOCADO</span>
      <span class="oil">OIL</span>
    </h1>

    <div class="tag">nothing else</div>

    <section class="claim-band">
      <p class="sub">from natural fruit</p>
      <p class="main">NOT GENETICALLY</p>
      <p class="main">ENGINEERED</p>
    </section>
    <div class="claim-tab">Healthy Eating</div>

    <div class="badge badge-left" role="img" aria-label="Cholesterol free badge"></div>
    <div class="badge badge-right" role="img" aria-label="Trans fat free badge"></div>

    <p class="caution">CAUTION: CONTENT UNDER PRESSURE</p>
    <p class="net">Net 5 FL. OZ. (147 ml)</p>
  </main>
</body>
</html>
```